Ru Pelko coffee capsule packaging 5 version

We want to redesign our current boxes for mirva lento compatible capsules. We are looking for something fresh, colorful, playful. We have 5 different types at the moment and attached you can find the current designs with the dimensions and necessary text.

deadline is to strict

```html
<!DOCTYPE html>
<html lang="en">
<head>
<meta charset="utf-8">
<title>Ru Pelko – Espresso capsule box</title>
<link rel="stylesheet" href="https://fonts.googleapis.com/css2?family=Poppins:wght@300;400;600&family=Quicksand:wght@300;500&display=swap">
<style>
  :root {
    --bg: #ececec;
    --ink: #262329;
    --purple: #9162b8;
    --purple-deep: #7a4d9b;
    --lilac: #c9a6e6;
    --crema: #d9a86c;
    --white: #ffffff;
  }
  * { margin: 0; padding: 0; box-sizing: border-box; }
  html, body { width: 1200px; height: 840px; overflow: hidden; }
  body {
    background: var(--bg);
    font-family: "Poppins", sans-serif;
    color: var(--white);
    position: relative;
  }
  .dieline {
    position: absolute;
    top: 150px;
    left: 100px;
    display: flex;
  }
  .panel {
    position: relative;
    width: 500px;
    height: 540px;
    overflow: hidden;
    background: var(--ink);
  }
  .panel__wave {
    position: absolute;
    left: 0; bottom: 0;
    width: 500px; height: 230px;
  }
  .panel__cap {
    position: absolute; left: 0; right: 0; top: 0; height: 18px;
    background: var(--purple);
  }
  .brand {
    position: absolute;
    top: 56px;
    font-weight: 600;
    font-size: 40px;
    letter-spacing: 1px;
    line-height: 1;
    color: var(--white);
  }
  .panel--front .brand { left: 40px; }
  .panel--side .brand { left: 0; right: 0; text-align: center; }
  .compat {
    position: absolute; top: 124px; left: 40px; width: 230px;
    text-align: center; font-size: 14px; line-height: 1.35; font-weight: 300;
  }
  .photo-capsule {
    position: absolute;
    border-radius: 28px;
    background: linear-gradient(160deg, var(--lilac) 0 55%, #1e1b21 100%);
  }
  .panel--front .photo-capsule { top: 196px; left: 50px; width: 160px; height: 150px; transform: rotate(-8deg); }
  .panel--side .photo-capsule { top: 150px; left: 330px; width: 140px; height: 150px; transform: rotate(6deg); }
  .photo-cup {
    position: absolute; top: 80px; left: 300px; width: 170px; height: 420px;
    border-radius: 85px;
    background: linear-gradient(rgba(255,255,255,0.08) 0 38%, var(--crema) 56%, #2b1a10 72%, var(--lilac) 100%);
  }
  .flavour {
    position: absolute; top: 384px; left: 40px;
    font-family: "Quicksand", sans-serif; font-weight: 300; font-size: 54px; line-height: 1;
  }
  .tagline {
    position: absolute; top: 452px; left: 40px; width: 220px; text-align: center;
    font-weight: 300; font-size: 22px; line-height: 1.2;
  }
  .tagline small { display: block; font-size: 15px; }
  .desc {
    position: absolute; top: 152px; left: 40px;
    font-size: 15px; line-height: 1.38; font-weight: 400;
  }
  .arrow { position: absolute; top: 232px; left: 170px; }
  .count {
    position: absolute; top: 284px; left: 40px;
    display: flex; align-items: center; gap: 8px; font-size: 28px; font-weight: 300;
  }
  .ingredients {
    position: absolute; top: 372px; left: 40px;
    font-size: 14px; line-height: 1.45; font-weight: 300;
  }
  .recycle { position: absolute; top: 424px; right: 36px; display: flex; gap: 8px; }
  .net-weight {
    position: absolute; top: 494px; left: 40px;
    display: flex; align-items: center; gap: 6px; font-size: 15px; font-weight: 300;
  }
</style>
</head>
<body>
  <div class="dieline">
    <section class="panel panel--front">
      <div class="panel__cap"></div>
      <svg class="panel__wave" viewBox="0 0 500 230" preserveAspectRatio="none" aria-hidden="true">
        <path d="M0 40 C 120 0, 260 80, 500 20 V230 H0 Z" fill="var(--purple)"/>
      </svg>
      <div class="brand">RU PELKO</div>
      <p class="compat">mirva lento®*compatible<br>compatibel/kompatibel</p>
      <div class="photo-capsule" role="img" aria-label="Espresso capsule photo"></div>
      <div class="photo-cup" role="img" aria-label="Steaming espresso in a double-walled glass"></div>
      <h1 class="flavour">espresso</h1>
      <p class="tagline">my cup of taste<small>115,2g℮</small></p>
    </section>

    <section class="panel panel--side">
      <svg class="panel__wave" viewBox="0 0 500 230" preserveAspectRatio="none" aria-hidden="true">
        <path d="M0 20 C 200 80, 340 0, 500 40 V230 H0 Z" fill="var(--purple-deep)"/>
      </svg>
      <div class="brand">RU PELKO</div>
      <p class="desc">Roasted and ground coffee<br>Café torréfié moulu<br>Gemalen gebrande koffie<br>Gemahlener Röstkaffee<br>Ristet og malet kaffe</p>
      <div class="photo-capsule" role="img" aria-label="Espresso capsule photo"></div>
      <svg class="arrow" width="130" height="70" viewBox="0 0 130 70" fill="none" stroke="#fff" stroke-width="4" stroke-linecap="round" stroke-linejoin="round" aria-hidden="true">
        <path d="M6 64 C 20 20, 70 6, 118 22"/>
        <path d="M104 8 L120 22 L102 34"/>
      </svg>
      <div class="count">
        <svg width="30" height="28" viewBox="0 0 30 28" aria-hidden="true"><path d="M1 2 H29 L24 24 H6 Z" fill="#fff"/></svg>
        <span>X16</span>
      </div>
      <p class="ingredients">Ingredients : roasted and ground coffee<br>Ingrédients : café torréfié moulu<br>Ingrediënten : gemalen gebrande koffie<br>Zutaten : Gemahlener Röstkaffee<br>Ingredienser : Ristet og malet kaffe</p>
      <div class="recycle" aria-label="Recycling and disposal icons">
        <svg width="30" height="30" viewBox="0 0 30 30" fill="none" stroke="#fff" stroke-width="3" stroke-linecap="round" aria-hidden="true">
          <path d="M25 15 A10 10 0 1 1 15 5"/><path d="M12 1 L16 5 L12 9"/>
        </svg>
        <svg width="24" height="30" viewBox="0 0 24 30" fill="none" stroke="#fff" stroke-width="3" stroke-linejoin="round" aria-hidden="true">
          <path d="M2 6 H22"/><path d="M5 6 L7 28 H17 L19 6"/>
        </svg>
      </div>
      <p class="net-weight">16
        <svg width="18" height="16" viewBox="0 0 30 28" aria-hidden="true"><path d="M1 2 H29 L24 24 H6 Z" fill="#fff"/></svg>
        x 7,2 gram = 115,2 gram℮</p>
    </section>
  </div>
</body>
</html>
```